Website design: Mobile Physiotherapy, Massage & Personal Training Business

I need a website that reflects a staff of health and fitness professionals. I would like the theme of the website to match the company logo (Summit Motion Wellness).
This is a link for a competitors website that I am fond of:
http://www.brackenrehab.com.au/
I am open to any and all creative and innovative designs.

```html
<!DOCTYPE html>
<html lang="en">
<head>
<meta charset="utf-8">
<title>Summit Motion Wellness</title>
<link href="https://fonts.googleapis.com/css2?family=Roboto+Condensed:wght@400;700&family=Open+Sans:wght@400;600&display=swap" rel="stylesheet">
<style>
:root{
  --red:#d42a33;
  --red-dark:#a8151d;
  --ink:#222;
  --body:#6b6b6b;
  --grey-band:#ececec;
  --footer:#3d3d3d;
  --footer-bottom:#2a2a2a;
  --side-head:#3f3f3f;
  --line:#e2e2e2;
}
*{margin:0;padding:0;box-sizing:border-box}
html,body{width:722px;height:1200px;overflow:hidden;background:#fff}
body{position:relative;font-family:"Open Sans",Arial,sans-serif;color:var(--body)}
.abs{position:absolute}
.header{left:0;top:0;width:722px;height:62px;background:#fff;border-top:3px solid var(--red)}
.brand{left:110px;top:22px;display:flex;align-items:center;gap:6px;font-family:"Roboto Condensed",sans-serif;font-weight:700;font-size:16px;color:var(--red)}
.brand-mark{width:10px;height:10px;background:var(--red)}
.account{left:504px;top:0;width:108px;height:17px;background:var(--red);border-radius:0 0 3px 3px;font-size:9px;color:#fff;text-align:center;line-height:17px}
.social{left:508px;top:29px;display:flex;gap:5px}
.social span{width:14px;height:14px;border-radius:50%;background:#3a3a3a}
.nav{left:0;top:62px;width:722px;height:32px;background:linear-gradient(#e0434b,#c3222b);display:flex;padding-left:110px}
.nav a{font-family:"Roboto Condensed",sans-serif;font-size:9.5px;color:#fff;text-decoration:none;line-height:32px;padding:0 16px;border-right:1px solid rgba(0,0,0,.15)}
.nav a.active{background:var(--red-dark)}
.hero{left:0;top:96px;width:722px;height:278px;background:linear-gradient(180deg,#8fb9e3 0%,#cfe0ee 38%,#8a9a78 55%,#6f6f6f 75%,#8e8e8e 100%)}
.hero-arrow{top:222px;width:28px;height:28px;border-radius:50%;background:rgba(255,255,255,.35);border:1px solid rgba(255,255,255,.6)}
.hero-dots{left:328px;top:348px;width:67px;height:22px;background:var(--red);border-radius:3px 3px 0 0;display:flex;justify-content:center;align-items:center;gap:4px}
.hero-dots span{width:5px;height:5px;border-radius:50%;background:#fff}
.post-title{left:110px;width:316px;font-family:"Roboto Condensed",sans-serif;font-weight:400;font-size:16px;color:var(--ink)}
.post-media{left:110px;width:316px}
.post-text{left:110px;width:316px;font-size:7.6px;line-height:12.6px}
.post-text p{margin-bottom:12.6px}
.post-text a{color:var(--red);text-decoration:none}
.sidebar{left:446px;top:397px;width:165px;border:1px solid var(--line)}
.side-head{background:var(--side-head);color:#fff;font-family:"Roboto Condensed",sans-serif;font-weight:700;font-size:10.5px;height:23px;line-height:23px;padding-left:8px}
.news{padding:11px 8px 8px;height:66px;border-bottom:1px solid var(--line);font-size:7px;line-height:10px}
.news h4{font-family:"Roboto Condensed",sans-serif;font-weight:400;font-size:8px;color:var(--red);margin-bottom:5px}
.news b{color:#333}
.side-more{background:#7b7b7b;color:#fff;font-size:7.5px;text-align:center;height:22px;line-height:22px}
.partners{left:0;top:958px;width:722px;height:80px;background:var(--grey-band)}
.badge{position:absolute;top:18px;height:42px;border-radius:4px}
.footer{left:0;top:1038px;width:722px;height:136px;background:var(--footer);color:#e8e8e8}
.foot-head{position:absolute;top:15px;font-family:"Roboto Condensed",sans-serif;font-weight:400;font-size:13px;color:#fff}
.foot-list{position:absolute;top:40px;list-style:none;font-size:7.5px;line-height:12.6px}
.contact-row{position:absolute;display:flex;gap:6px;font-size:7.5px;line-height:11px}
.copyright{left:0;top:1174px;width:722px;height:26px;background:var(--footer-bottom);color:#ccc;font-size:7.5px;text-align:center;line-height:26px}
</style>
</head>
<body>

<header class="abs header">
  <div class="abs brand"><span class="brand-mark"></span>Summit Motion Wellness</div>
  <div class="abs account">Login &nbsp;|&nbsp; Signup</div>
  <div class="abs social"><span></span><span></span><span></span><span></span><span></span><span></span></div>
</header>

<nav class="abs nav">
  <a class="active">HOME</a><a>ABOUT US</a><a>OUR SERVICES</a><a>OUR PRODUCTS</a><a>CONTACT US</a>
</nav>

<section class="abs hero" role="img" aria-label="Group of cyclists riding along a sunny coastal road"></section>
<div class="abs hero-arrow" style="left:27px"></div>
<div class="abs hero-arrow" style="left:667px"></div>
<div class="abs hero-dots"><span></span><span></span><span></span><span></span><span></span></div>

<h2 class="abs post-title" style="top:394px">Lorem Ipsum Dollar Sit Emmet Ponto Gravida</h2>
<div class="abs post-media" style="top:420px;height:101px;background:linear-gradient(180deg,#9cc3e6,#c8d6c0 45%,#7b7b73)" role="img" aria-label="Cyclists on a road"></div>
<div class="abs post-text" style="top:533px">
  <p>This is a sample version of Lorem Ipsum. Proin gravida nibh vel velit auctor aliquet. Aenean sollicitudin, lorem quis bibendum auctor, nisi elit consequat ipsum, nec sagittis sem nibh id elit. Duis sed odio sit amet nibh vulputate cursus a sit amet mauris. Morbi accumsan ipsum velit. Nam nec tellus a odio tincidunt auctor a ornare odio.</p>
  <p>Sed non mauris vitae erat consequat auctor eu in elit. Class aptent taciti sociosqu ad litora torquent per conubia nostra, per inceptos himenaeos. Mauris in erat justo. Nullam ac urna eu felis dapibus condimentum sit amet a augue. Sed non neque elit. Sed ut imperdiet nisi. Proin condimentum fermentum nunc. <a>Read More &rarr;</a></p>
</div>

<h2 class="abs post-title" style="top:668px">Lorem Ipsum Dollar Sit Emmet Ponto Gravida</h2>
<div class="abs post-media" style="top:695px;height:100px;background:linear-gradient(160deg,#4a4a4a,#1c1c1c)" role="img" aria-label="Video still of a cyclist on a dark road">
  <svg width="316" height="100" viewBox="0 0 316 100"><circle cx="158" cy="50" r="18" fill="none" stroke="#fff" stroke-width="2"/><path d="M152 40 L168 50 L152 60Z" fill="#fff"/></svg>
</div>
<div class="abs post-text" style="top:807px">
  <p>This is a sample version of Lorem Ipsum. Proin gravida nibh vel velit auctor aliquet. Aenean sollicitudin, lorem quis bibendum auctor, nisi elit consequat ipsum, nec sagittis sem nibh id elit. Duis sed odio sit amet nibh vulputate cursus a sit amet mauris. Morbi accumsan ipsum velit. Nam nec tellus a odio tincidunt auctor a ornare odio.</p>
  <p>Sed non mauris vitae erat consequat auctor eu in elit. Class aptent taciti sociosqu ad litora torquent per conubia nostra, per inceptos himenaeos. Mauris in erat justo. Nullam ac urna eu felis dapibus condimentum sit amet a augue. Sed non neque elit. Sed ut imperdiet nisi. Proin condimentum fermentum nunc. <a>Read More &rarr;</a></p>
</div>

<aside class="abs sidebar">
  <div class="side-head">Latest News</div>
  <div class="news"><h4>Lorem Ipsum Dollar Sit Emet Ponto Gravida</h4><b>Sunday - 15 April:</b> version of Lorem Ipsum. Proin gravida nibh vel velit auctor aliquet. Aenean sollicitudin, lorem quis.</div>
  <div class="news"><h4>Lorem Ipsum Dollar Sit Emet Ponto Gravida</h4><b>Sunday - 15 April:</b> version of Lorem Ipsum. Proin gravida nibh vel velit auctor aliquet. Aenean sollicitudin, lorem quis.</div>
  <div class="news"><h4>Lorem Ipsum Dollar Sit Emet Ponto Gravida</h4><b>Sunday - 15 April:</b> version of Lorem Ipsum. Proin gravida nibh vel velit auctor aliquet. Aenean sollicitudin, lorem quis.</div>
  <div class="news"><h4>Lorem Ipsum Dollar Sit Emet Ponto Gravida</h4><b>Sunday - 15 April:</b> version of Lorem Ipsum. Proin gravida nibh vel velit auctor aliquet. Aenean sollicitudin, lorem quis.</div>
  <div class="side-more">View More News</div>
</aside>

<section class="abs partners" aria-label="Partner associations">
  <div class="badge" style="left:110px;width:160px;background:#2f7fc0"></div>
  <div class="badge" style="left:290px;width:30px;background:#2a3f8a"></div>
  <div class="badge" style="left:340px;width:40px;background:#1d5fa6"></div>
  <div class="badge" style="left:400px;width:60px;background:#f0a020"></div>
  <div class="badge" style="left:479px;width:38px;background:#20407a"></div>
  <div class="badge" style="left:536px;width:76px;background:#5a2a6a"></div>
</section>

<footer class="abs footer">
  <h3 class="foot-head" style="left:110px">OUR SERVICES</h3>
  <ul class="foot-list" style="left:110px"><li>Physio/Sports Physio</li><li>Massage/Soft Tissue</li><li>Physio Pilates/Pilates</li><li>Dietetics/Nutrition</li><li>Podiatry</li></ul>
  <ul class="foot-list" style="left:196px"><li>Sport Psychology</li><li>Bounce Back Spinal Stability Classes</li><li>Running Made Easy</li><li>Run Technique Clinic</li></ul>
  <h3 class="foot-head" style="left:341px">OUR PRODUCTS</h3>
  <ul class="foot-list" style="left:341px"><li>Pro Compression Range</li><li>Home Exercise Equipment</li><li>Postural Aids</li><li>Self Treatment Products</li><li>Braces &amp; Tape</li></ul>
  <h3 class="foot-head" style="left:472px">CONTACT US</h3>
  <div class="contact-row" style="left:472px;top:41px">
    <svg width="9" height="9" viewBox="0 0 10 10"><path d="M2 1l2 2-1 1.5c.8 1.5 1.5 2.2 3 3L7.5 6l2 2-1.5 1.5C4 9 1 6 .5 1.5Z" fill="#ddd"/></svg>000 555 0142</div>
  <div class="contact-row" style="left:472px;top:58px">
    <svg width="10" height="8" viewBox="0 0 10 8"><rect x=".5" y=".5" width="9" height="7" fill="none" stroke="#ddd"/><path d="M.5 .5L5 4.5 9.5.5" fill="none" stroke="#ddd"/></svg>info@summitmotion.com</div>
  <div class="contact-row" style="left:472px;top:75px">
    <svg width="9" height="11" viewBox="0 0 9 11"><path d="M4.5 0A4 4 0 0 1 8.5 4c0 3-4 7-4 7S.5 7 .5 4A4 4 0 0 1 4.5 0Z" fill="#ddd"/><circle cx="4.5" cy="4" r="1.5" fill="#3d3d3d"/></svg><span>1420 Harbour Lane &nbsp;Address Goes Here<br>New Jersey</span></div>
</footer>
<div class="abs copyright">Copyright 2014 - All Rights Reserved</div>

</body>
</html>
```